Restwell Nook at exhibiton 2019

We are going to an exhibition where the main customers are head of purchasing department in airlines and railways companies. Our selling product is Restwell Nook, take a look at our website: www.restwellnook.no
Restwell Nook provides full support to your head while seated, soft and smooth, so you can sleep without whiplash and falling into the lap of your neighbor. “Enjoy a good sleep while seated”.
The wall display will be approximant size/print area: width 3200mm * height 2250mm
The wall display has to content the uploaded pictures, and can be cropped.
One of the pictures has the seat strap around the whole part of the seat. This picture has to be changed. The part of the seat strap has to be changed as the picture where the seat strap goes only around the inner pillow/headrest pillow. Why this is important has to do with the screen behind the seat, which cannot be disturbed.
Example how the wall display could looks, if I think it out loud: pictures of travelers at airports/railway station, travelers who are exhausted, tired, pictures of trains and planes in motion.
Words and slogans which can be used to the designer’s toolbox:
• Physiotherapists recommends Restwell Nook
• Enjoy a good sleep while seated
• Sleep safely with your head fully supported, avoid whiplash
• Arrive at your destination fresh and rested
• Restwell Nook makes your journey more comfortable
• Restwell Nook upgrades you to sleeping class
• Restwell Nook provides full support to your head while seated, soft and smooth, sleep safe without falling into the lap of your neighbor
• Headrest pillow gives a lot of whiplashes
I did upload logo, colors and different pictures of the product to your toolbox.

```html
<!DOCTYPE html>
<html lang="en">
<head>
<meta charset="utf-8">
<title>Restwell Nook – Exhibition Wall</title>
<link rel="stylesheet" href="https://fonts.googleapis.com/css2?family=Josefin+Sans:wght@400&family=Montserrat:wght@700;800&display=swap">
<style>
  :root {
    --ink: #231f20;
    --orange: #f9a825;
    --white: #ffffff;
    --cabin-cream: #e9ddcc;
    --cabin-warm: #cdb59a;
    --seat-red: #b3282d;
  }
  * { margin: 0; padding: 0; box-sizing: border-box; }
  html, body { width: 1200px; height: 770px; overflow: hidden; background: #f2f2f2; }
  .wall-display {
    position: relative;
    width: 1200px;
    height: 770px;
    background: var(--ink);
    overflow: hidden;
    font-family: "Montserrat", sans-serif;
  }
  .wall-art { position: absolute; inset: 0; }
  .brand-name {
    position: absolute;
    left: 0; width: 528px; top: 92px;
    text-align: center;
    font-family: "Josefin Sans", sans-serif;
    font-weight: 400;
    font-size: 44px;
    line-height: 1;
    letter-spacing: 4px;
    color: var(--orange);
    text-transform: uppercase;
  }
  .slogan {
    position: absolute;
    left: 0; top: 0;
    width: 100%; height: 100%;
    color: var(--white);
    text-transform: uppercase;
    line-height: 1;
    pointer-events: none;
  }
  .slogan span {
    position: absolute;
    left: 83px;
    white-space: nowrap;
    line-height: 1;
  }
  .slogan__lead { top: 238px; font-size: 92px; font-weight: 800; letter-spacing: 1px; }
  .slogan__line { font-size: 46px; font-weight: 700; letter-spacing: 0.3px; }
  .slogan__line--first { top: 321px; }
  .slogan__line--second { top: 363px; }
  .web-address {
    position: absolute;
    left: 0; width: 1200px; top: 650px;
    text-align: center;
    font-weight: 800;
    font-size: 40px;
    line-height: 1;
    color: var(--ink);
    letter-spacing: 0.5px;
  }
  .web-address__name { color: var(--white); }
</style>
</head>
<body>
<main class="wall-display">
  <svg class="wall-art" width="1200" height="770" viewBox="0 0 1200 770" xmlns="http://www.w3.org/2000/svg">
    <defs>
      <linearGradient id="cabinTones" x1="0" y1="0" x2="1" y2="1">
        <stop offset="0" stop-color="var(--cabin-cream)"/>
        <stop offset="0.45" stop-color="var(--cabin-warm)"/>
        <stop offset="0.8" stop-color="var(--seat-red)"/>
        <stop offset="1" stop-color="#e8d9d2"/>
      </linearGradient>
      <radialGradient id="strapTones"><stop offset="0" stop-color="#6b6b6b"/><stop offset="1" stop-color="#e4e1dc"/></radialGradient>
      <radialGradient id="pillowTones"><stop offset="0" stop-color="#e09b1a"/><stop offset="0.5" stop-color="#1e1e1e"/><stop offset="1" stop-color="#0e0e0e"/></radialGradient>
      <radialGradient id="pouchTones"><stop offset="0" stop-color="#4a2d20"/><stop offset="1" stop-color="#dcd8d2"/></radialGradient>
    </defs>

    <!-- travel photo area -->
    <path class="travel-photo" role="img" aria-label="Photo: passengers in an aircraft cabin sleeping upright in red seats, heads supported by the headrest strap"
          d="M702 0 C610 90 572 220 586 360 C596 450 640 515 700 556 L1200 546 L1200 0 Z" fill="url(#cabinTones)"/>
    <path class="photo-frame-arc" d="M686 0 C594 95 556 225 572 370 C580 440 610 495 640 520" fill="none" stroke="var(--orange)" stroke-width="2"/>

    <!-- quote rules and marks -->
    <g class="quote-rules" fill="var(--orange)">
      <rect x="112" y="232" width="335" height="2"/>
      <text x="83" y="258" font-family="Montserrat, sans-serif" font-weight="800" font-size="58">“</text>
      <rect x="86" y="415" width="318" height="2"/>
      <text x="404" y="460" font-family="Montserrat, sans-serif" font-weight="800" font-size="58">”</text>
    </g>

    <!-- bottom band -->
    <path class="band-white" d="M0 656 C200 600 420 560 640 548 C820 540 1000 538 1200 534 L1200 770 L0 770 Z" fill="var(--white)"/>
    <path class="band-orange" d="M0 672 C200 618 420 580 640 566 C820 556 1000 553 1200 552 L1200 770 L0 770 Z" fill="var(--orange)"/>
    <path class="band-line" d="M0 650 C150 610 330 575 500 560" fill="none" stroke="var(--white)" stroke-width="2"/>

    <!-- product photo circles -->
    <circle class="product-photo" role="img" aria-label="Photo: the seat strap with its buckle" cx="584" cy="388" r="84" fill="url(#strapTones)" stroke="var(--orange)" stroke-width="2"/>
    <circle class="product-photo" role="img" aria-label="Photo: the black headrest pillow with orange tab" cx="517" cy="522" r="104" fill="url(#pillowTones)" stroke="var(--orange)" stroke-width="2"/>
    <circle class="product-photo" role="img" aria-label="Photo: brown drawstring storage pouch" cx="684" cy="520" r="90" fill="url(#pouchTones)" stroke="var(--orange)" stroke-width="2"/>

    <!-- web address underline -->
    <rect class="web-underline" x="550" y="702" width="108" height="4" fill="var(--white)"/>
  </svg>

  <div class="brand-name">Restwell Nook</div>

  <h1 class="slogan">
    <span class="slogan__lead">Enjoy</span>
    <span class="slogan__line slogan__line--first">A good sleep</span>
    <span class="slogan__line slogan__line--second">while seated</span>
  </h1>

  <p class="web-address">www.<span class="web-address__name">restwellnook</span>.no</p>
</main>
</body>
</html>
```